New Jar Label for Manuka Honey Company!

Ka Rito Honey, a Manuka Honey company from New Zealand is looking for a fresh & engaging label for our manuka honey jars.

Attached are some examples of label designs that we like, feel free to use the language/copy on these labels for inspiration/content/copy, but feel free to add your own creative spin if you have a great design idea!

LABEL DIMENSIONS: 1654mmx532mm

Label Must Include:
- MGO rating
- Made (or) Product of New Zealand
- Manuka Honey (can add extra text similar to attached examples)

Label Can Include:
- Badges: raw food, non gmo, bpa free, gluten free, halal etc
- anything you feel is appropriate

You can change the color of the logo(s) to Black, White, Silver or Gold.

Can you please include a mockup of your label design(s) on the supplied "Jar Mockup File". You can change the scene of the mockup if you like.

UPDATE:

Have decided on bee logo so please bo longer use the mountain logo for label mockups. Design(s) will need multiple color variations to represent the other MGO ratings, flavor combos and other honey types, other than manuka.

• Provide multiple designs for each honey type
Manuka Design
Spring Honey Design
MGO 100-1000 Design(s)
Wildflower Honey Design
Flavor Combo Honey Design

```html
<!DOCTYPE html>
<html lang="en">
<head>
<meta charset="utf-8">
<title>Ka Rito Honey – Manuka Label</title>
<link href="https://fonts.googleapis.com/css2?family=Montserrat:wght@400;600&family=Oswald:wght@300;500&display=swap" rel="stylesheet">
<style>
  :root {
    --backdrop: #b99a44;
    --label-dark: #2b2b2b;
    --label-mid: #4a4a4a;
    --band-dark: #3a3a3a;
    --ice: #d6f1f8;
    --gold: #e0b22a;
    --gold-deep: #c9961c;
    --white: #ffffff;
    --ink: #3b4a50;
    --tag-bg: #2f3233;
  }
  * { margin: 0; padding: 0; box-sizing: border-box; }
  html, body { width: 1200px; height: 824px; overflow: hidden; }
  body {
    background: var(--backdrop);
    font-family: "Montserrat", sans-serif;
    position: relative;
  }
  .label {
    position: absolute;
    left: 100px; top: 250px;
    width: 1000px; height: 322px;
    background: linear-gradient(90deg, var(--label-dark) 0%, var(--label-mid) 45%, var(--label-dark) 100%);
  }
  .hex-band {
    position: absolute; left: 0; top: 0;
    width: 100%; height: 56px;
    background: linear-gradient(180deg, var(--band-dark), #555);
    border-top: 2px solid var(--ice);
    border-bottom: 2px solid var(--ice);
  }
  .hex-field {
    position: absolute; left: 0; top: 56px;
    width: 100%; height: 266px;
    background: radial-gradient(ellipse at 30% 50%, #585858 0%, #333 70%);
  }
  .brand-seal {
    position: absolute; left: 50%; top: 28px;
    transform: translateX(-50%);
    width: 64px; height: 64px;
    border-radius: 50%;
    background: radial-gradient(circle at 40% 35%, var(--gold), var(--gold-deep));
    display: flex; align-items: center; justify-content: center;
    text-align: center;
  }
  .brand-name {
    font-weight: 600; font-size: 9px; line-height: 1.1;
    color: var(--white);
    letter-spacing: 0.5px;
  }
  .gluten-free {
    position: absolute; left: 360px; top: 120px;
    font-family: "Oswald", sans-serif;
    color: var(--ice);
    line-height: 0.95;
  }
  .gluten-free .top { font-weight: 500; font-size: 10px; display: block; }
  .gluten-free .bottom { font-weight: 300; font-size: 12px; display: block; }
  .title {
    position: absolute; left: 0; width: 100%; top: 144px;
    text-align: center;
    font-weight: 600; font-size: 30px; letter-spacing: 5px;
    color: var(--white);
  }
  .subtitle {
    position: absolute; left: 0; width: 100%; top: 184px;
    font-weight: 400; font-size: 10px; letter-spacing: 0.5px;
    color: var(--white);
    display: flex; justify-content: center; align-items: center; gap: 8px;
  }
  .subtitle .rule { width: 12px; height: 1.5px; background: var(--white); display: inline-block; }
  .badges {
    position: absolute; left: 0; width: 100%; top: 210px;
    display: flex; justify-content: center; gap: 14px;
  }
  .badge {
    width: 28px; height: 28px; border-radius: 50%;
    background: var(--ice);
    display: flex; align-items: center; justify-content: center;
    text-align: center;
    font-size: 5.5px; line-height: 1.05; font-weight: 400;
    color: var(--ink);
  }
  .mgo-rating {
    position: absolute; left: 0; width: 100%; top: 248px;
    text-align: center;
    font-weight: 600; font-size: 8px; letter-spacing: 1.5px;
    color: var(--gold);
  }
  .origin {
    position: absolute; left: 0; width: 100%; top: 262px;
    text-align: center;
    font-size: 5.5px; line-height: 1.3;
    color: var(--white);
  }
  .net-weight {
    position: absolute; left: 50%; top: 284px;
    transform: translateX(-50%);
    width: 100px; height: 11px;
    background: var(--tag-bg);
    text-align: center;
    font-size: 4.5px; letter-spacing: 1px; line-height: 11px;
    color: var(--gold);
  }
</style>
</head>
<body>
  <section class="label">
    <div class="hex-band" role="img" aria-label="Honeycomb outline pattern band in ice blue on charcoal"></div>
    <div class="hex-field" role="img" aria-label="Faint honeycomb pattern on dark charcoal background"></div>

    <div class="brand-seal">
      <span class="brand-name">KA RITO<br>HONEY</span>
    </div>

    <p class="gluten-free"><span class="top">GLUTEN</span><span class="bottom">FREE!</span></p>

    <h1 class="title">MANUKA</h1>
    <p class="subtitle"><span class="rule"></span>RAW MANUKA HONEY<span class="rule"></span></p>

    <div class="badges">
      <span class="badge">BPA<br>FREE</span>
      <span class="badge">NON<br>GMO</span>
      <span class="badge">HALAL</span>
    </div>

    <p class="mgo-rating">MGO 100+</p>
    <p class="origin">PRODUCT OF NEW ZEALAND<br>100% PURE MANUKA HONEY</p>
    <p class="net-weight">250mg | 8.0 oz</p>
  </section>
</body>
</html>
```